Integrative Medical Practice Website Redo

I am needing to have our current website redesigned to make it a responsive website to work on smartphones.
Current website
www.brightoakfm.com
Here are several examples of what I am looking for
https://www.corvanhealth.com/
I am wanting a popup for a newsletter signup
Looking for a very professional, clean, simple, minimalist, bold well designed website
Colors would ideally be greens and blues, cool tones, muted colors, or graytones like:
https://journeybright.org/
Several other clean design examples
http://7harborsrenton.com/
http://www.belvomedical.com/
http://sunpathyouth.com/
http://yourcellduke.com/
I would like the top navigation bar to be able to slide down while browsing site
We are also needing to add several features that are not on our current website:
Questionnaire buttons
Are you toxic questionnaire?
Take our hormone quiz to find out if hormones are affecting your health.
online scheduling option for:
nutrition counselling
testing like body composition, basal metabolic rate, CIMT, breast thermography, VO2 Max testing, Vita Trace
Therapies like whole body vibration, infrared sauna, Exercise with oxygen, hyperbaric oxygen, spinal decompression
Need to have separate page for different services and split up services into:
Consults/Office Visits, Testing, Therapies, Procedures
Need to have a button link to patient portal
Needs to have online store
Need to add navigation button "Start Here"
Need a spot for a video on practice summary
Newsletter signup to collect emails
Testimonials from linkpage
Blog that posts can be shared with social media
Password protected patient access that can integrate into crate.net ideally
Modules for programs online classes/videos
I have attached stock images that you can use, but feel free to find others to use.
I have also attached a copy of our current brochure that shows an overview of the practice
Target Market(s)
Health conscious people of all ages looking for a family medicine doctor
Industry/Entity Type
Alternative Medicine
Coding
Coded - Design and coding required
Number of Pages Required
5+ page
Look and feel

```html
<!DOCTYPE html>
<html lang="en">
<head>
<meta charset="utf-8">
<title>Bright Oak Family Medicine</title>
<link href="https://fonts.googleapis.com/css2?family=Josefin+Sans:wght@300;400;600&family=Bree+Serif&family=Open+Sans:ital,wght@0,400;0,600;1,400&display=swap" rel="stylesheet">
<style>
:root{
  --blue:#3aa3d9;
  --blue-dark:#2b8fc4;
  --green:#9cc53a;
  --green-light:#b7d65e;
  --gray-bg:#eeeeee;
  --text:#555;
  --white:#fff;
}
*{margin:0;padding:0;box-sizing:border-box}
html,body{width:1200px;height:4348px;overflow:hidden}
body{font-family:"Open Sans",sans-serif;color:var(--text);background:var(--white);font-size:14px}
.wrap{width:1044px;margin:0 auto;position:relative;height:100%}
section,header,footer,nav{position:relative;overflow:hidden}
.sec-title{font-family:"Josefin Sans",sans-serif;font-weight:400;font-size:48px;text-align:center;color:var(--blue);letter-spacing:1px;text-transform:uppercase}
.sec-title .hl{color:var(--green)}
.btn{display:inline-block;background:var(--blue);color:var(--white);font-family:"Open Sans",sans-serif;text-transform:uppercase;font-size:19px;padding:12px 26px;border-radius:3px;letter-spacing:.5px;white-space:nowrap}

/* header */
.site-header{height:122px;background:var(--white)}
.brand{position:absolute;left:0;top:18px;display:flex;align-items:center;gap:12px}
.brand-dot{width:44px;height:44px;border-radius:50%;background:var(--green)}
.brand-name{font-family:"Bree Serif",serif;color:var(--blue);font-size:34px;line-height:1}
.brand-name small{display:block;font-size:16px;letter-spacing:3px;margin-top:4px}
.cart{position:absolute;right:80px;top:14px;font-size:14px;color:#444;display:flex;gap:6px;align-items:center}
.search{position:absolute;right:6px;top:12px}
.phone{position:absolute;right:190px;top:62px;display:flex;align-items:center;gap:12px;font-size:20px;color:#444}
.phone-ic{width:46px;height:46px;border-radius:50%;border:2px solid var(--blue);display:flex;align-items:center;justify-content:center}
.start-here{position:absolute;right:0;top:54px;font-size:20px;padding:12px 20px}

/* nav */
.main-nav{height:64px;background:var(--green)}
.main-nav ul{list-style:none;display:flex;height:64px;align-items:center;font-size:14px;text-transform:uppercase;color:var(--white)}
.main-nav li{padding:0 12px;height:64px;line-height:64px;white-space:nowrap}
.main-nav li.active{background:var(--blue);padding:0 26px}

/* hero */
.hero{height:524px}
.hero-photo{position:absolute;inset:0;background:linear-gradient(180deg,#9fc4d6 0%,#c8dbe2 40%,#8fa16a 65%,#e9ece0 80%,#7a8b4e 100%)}
.hero-copy{position:absolute;left:78px;top:150px;width:600px}
.hero-copy h1{font-family:"Bree Serif",serif;font-weight:400;font-size:44px;line-height:1.2;color:#1d2a30}
.hero-copy p{font-style:italic;font-size:18px;color:#3b4d54;margin:10px 0 26px;line-height:1.3}
.hero-copy .btn{font-size:22px}
.slide-arrow{position:absolute;top:388px;width:48px;height:48px;border-radius:50%;border:2px solid rgba(255,255,255,.8);background:rgba(255,255,255,.25)}
.slide-arrow.prev{left:14px}.slide-arrow.next{right:14px}

/* welcome */
.welcome{height:310px;background:var(--blue);color:var(--white);text-align:center}
.welcome .sec-title{color:var(--white);padding-top:52px}
.welcome p{width:1000px;margin:22px auto 0;font-size:14.5px;line-height:1.8}

/* services */
.services{height:750px;background:var(--gray-bg)}
.services .sec-title{padding-top:56px}
.service-grid{display:grid;grid-template-columns:repeat(4,252px);gap:16px 12px;margin-top:24px}
.service{height:232px;background:var(--white)}
.service-img{height:166px}
.service-label{height:66px;background:var(--green);color:var(--white);text-transform:uppercase;font-size:17px;display:flex;align-items:center;justify-content:center;text-align:center;line-height:1.3;padding:0 20px}
.view-all{position:absolute;left:50%;transform:translateX(-50%);top:648px;font-size:22px}

/* formula */
.formula{height:347px}
.formula .sec-title{padding-top:60px}
.habits{display:flex;justify-content:space-between;width:870px;margin:44px auto 0}
.habit{width:150px;text-align:center}
.habit-ic{width:116px;height:116px;border-radius:50%;background:var(--green);border:5px solid var(--blue);margin:0 auto 18px;display:flex;align-items:center;justify-content:center}
.habit span{font-family:"Josefin Sans",sans-serif;font-size:18px;color:#444;text-transform:capitalize}

/* scheduling */
.scheduling{height:363px;background:linear-gradient(100deg,var(--green) 0%,var(--green-light) 55%,#cfe58e 100%);color:var(--white)}
.scheduling .sec-title{text-align:left;padding:64px 0 0 74px;font-size:48px;color:var(--white)}
.scheduling .sec-title .hl{color:var(--blue)}
.scheduling p{position:absolute;left:114px;top:122px;width:580px;font-size:15.5px;line-height:1.6}
.scheduling .btn{position:absolute;left:176px;top:256px;font-size:22px}
.sched-photo{position:absolute;right:0;top:0;width:400px;height:363px;background:radial-gradient(ellipse at 60% 55%,#f1e3d5 0%,#d9c2a6 35%,#b8d36e 75%,transparent 100%)}

/* about */
.about{height:478px}
.about .sec-title{padding-top:50px}
.doctors{display:flex;justify-content:space-between;margin-top:46px}
.doctor{width:502px;display:flex;gap:22px}
.doctor-photo{width:212px;height:258px;flex:none}
.doctor h3{font-family:"Josefin Sans",sans-serif;font-weight:400;font-size:26px;color:var(--green);text-transform:uppercase;margin-bottom:6px}
.doctor h3 span{color:var(--blue)}
.doctor p{font-size:14.5px;line-height:1.75;color:#444}
.doctor .btn{margin-top:18px;font-size:22px;padding:10px 22px}

/* testimonial */
.testimonial{height:508px;background:linear-gradient(135deg,#3aa3d9 0%,#5ab6e2 50%,#3a9fd3 100%);color:var(--white);text-align:center}
.testimonial .sec-title{color:var(--white);padding-top:52px}
.client-photo{width:112px;height:112px;border-radius:50%;border:4px solid var(--white);background:linear-gradient(#d8e6ee,#8aa6b6);margin:18px auto 0}
.testimonial blockquote{width:1010px;margin:30px auto 0;font-size:14.5px;line-height:1.8}
.client-name{margin-top:14px;font-family:"Josefin Sans",sans-serif;font-size:22px;color:var(--green);text-transform:uppercase}
.client-name::before,.client-name::after{content:"";display:inline-block;width:34px;height:2px;background:var(--green);vertical-align:middle;margin:0 12px}
.dots{display:flex;justify-content:center;gap:8px;margin-top:16px}
.dots i{width:10px;height:10px;border-radius:50%;border:1.5px solid var(--white)}
.dots i.on{background:var(--white)}

/* widgets */
.widgets{height:507px;background:var(--gray-bg)}
.widget-row{display:flex;justify-content:space-between;padding-top:34px}
.widget{width:340px;height:434px;background:var(--white)}
.widget h4{height:58px;line-height:62px;background:var(--green);color:var(--white);font-family:"Josefin Sans",sans-serif;font-weight:400;font-size:26px;padding-left:20px;text-transform:uppercase}
.feature-list{padding:26px 20px 0}
.feature-item{display:flex;gap:14px;font-size:16px;color:#444;line-height:1.5;margin-bottom:22px}
.feature-item i{flex:none;width:14px;height:22px;border-radius:50% 0;background:var(--green);margin-top:2px}
.quiz-btn{margin:12px 0 0 36px;display:flex;width:256px;height:58px}
.quiz-btn b{flex:1;background:var(--blue);color:var(--white);font-weight:400;font-size:21px;display:flex;align-items:center;justify-content:center;text-transform:uppercase}
.quiz-btn em{width:40px;background:var(--green);display:flex;align-items:center;justify-content:center}
.blog-list{padding:18px 0 0 0}
.post{display:flex;gap:14px;margin-bottom:16px}
.post-img{width:134px;height:96px;flex:none}
.post h5{font-family:"Bree Serif",serif;font-weight:400;color:var(--blue);font-size:17px;letter-spacing:.5px}
.post p{font-size:14px;line-height:1.5;color:#666}
.feed{padding:14px 18px}
.feed-note{font-size:14px;color:#444;margin-bottom:10px}
.feed-box{border:1px solid #ddd;height:310px;position:relative}
.feed-head{display:flex;gap:10px;padding:12px}
.feed-thumb{width:62px;height:62px;background:linear-gradient(#e6c9a0,#b98c57);flex:none}
.feed-head b{font-family:"Bree Serif",serif;font-weight:400;color:var(--blue);font-size:17px;line-height:1.2;display:block}
.feed-head span{font-size:13px;color:#777}
.feed-text{padding:0 12px;font-size:15px;color:#333}
.feed-img{height:148px;margin:10px 12px 0;background:linear-gradient(135deg,#5a3048,#a33a4a 45%,#3e4f2a)}
.feed-foot{position:absolute;bottom:8px;left:12px;right:12px;display:flex;justify-content:space-between;font-size:13px;color:var(--green)}

/* footer */
.site-footer{height:342px;background:var(--green);color:var(--white);border-top:4px solid var(--blue)}
.foot-cols{display:flex;padding-top:40px}
.foot-col{width:261px}
.foot-col h6{font-family:"Josefin Sans",sans-serif;font-weight:400;font-size:21px;text-transform:uppercase;margin-bottom:18px;letter-spacing:.5px}
.links{list-style:none;font-size:14px;line-height:1.6}
.links li::before{content:"";display:inline-block;width:7px;height:7px;border-radius:50%;background:var(--white);margin-right:12px;vertical-align:middle}
.contact-row{display:flex;gap:14px;font-size:14px;line-height:1.5;margin-bottom:14px}
.contact-row svg{flex:none;margin-top:2px}
.hours-row{display:flex;font-size:14px;margin-bottom:14px;align-items:center}
.hours-row i{width:18px;height:18px;border-radius:50%;border:2px solid var(--white);margin-right:14px;flex:none}
.hours-row span:first-of-type{width:112px}
.hours-note{font-size:13.5px;line-height:1.5;text-align:center;width:230px}
.news p{font-size:14px;line-height:1.5;margin-bottom:12px}
.news .field{height:44px;background:var(--white);color:#999;font-size:14px;padding:12px;width:240px}
.news .btn{margin-top:20px;font-size:20px;padding:10px 22px}
.bottom-bar{height:33px;background:var(--blue);color:var(--white);text-align:center;font-size:13px;line-height:33px}
.bottom-bar b{color:var(--green);font-weight:600}
</style>
</head>
<body>

<header class="site-header">
  <div class="wrap">
    <div class="brand">
      <span class="brand-dot"></span>
      <span class="brand-name">Bright Oak<small>FAMILY MEDICINE</small></span>
    </div>
    <div class="cart">
      <svg width="22" height="18" viewBox="0 0 22 18"><path d="M1 2h4l3 10h10l3-7H7" fill="none" stroke="#3aa3d9" stroke-width="2"/><circle cx="9" cy="15.5" r="1.8" fill="#3aa3d9"/><circle cx="17" cy="15.5" r="1.8" fill="#3aa3d9"/></svg>
      My Cart
    </div>
    <div class="search"><svg width="22" height="22" viewBox="0 0 22 22"><circle cx="9" cy="9" r="6.5" fill="none" stroke="#3aa3d9" stroke-width="2.5"/><path d="M14 14l6 6" stroke="#3aa3d9" stroke-width="3"/></svg></div>
    <div class="phone">
      <span class="phone-ic"><svg width="22" height="22" viewBox="0 0 24 24"><path d="M6.6 10.8a15 15 0 006.6 6.6l2.2-2.2a1 1 0 011-.25 11.4 11.4 0 003.6.57 1 1 0 011 1V20a1 1 0 01-1 1A17 17 0 013 4a1 1 0 011-1h3.5a1 1 0 011 1 11.4 11.4 0 00.57 3.6 1 1 0 01-.25 1z" fill="#3aa3d9"/></svg></span>
      (555) 214-7730
    </div>
    <span class="btn start-here">Start Here</span>
  </div>
</header>

<nav class="main-nav">
  <div class="wrap">
    <ul>
      <li class="active">Home</li><li>About Us</li><li>Services</li><li>Resources</li><li>FAQ</li><li>Current Patients</li><li>New Patients</li><li>OakWell Membership</li><li>Contact Us</li>
    </ul>
  </div>
</nav>

<section class="hero">
  <div class="hero-photo" role="img" aria-label="Family walking through a meadow of white flowers beside a lake with mountains"></div>
  <div class="hero-copy">
    <h1>Helping you get well, stay well, and live well</h1>
    <p>Restoring your Health Naturally with Nutrition, Manipulation, Acupuncture and Integrative Medicine</p>
    <span class="btn">Contact Us Now</span>
  </div>
  <span class="slide-arrow prev"></span><span class="slide-arrow next"></span>
</section>

<section class="welcome">
  <h2 class="sec-title">Welcome to <span class="hl">Bright Oak</span></h2>
  <p>Welcome to our website. As an integrative medical practice, we provide innovative, quality family health care by uniquely combining both conventional and alternative medicine. Our aim is to treat the whole patient not just the symptoms. This "best of both worlds" approach provides patients with options in the management of their concerns while addressing the underlying cause of their illness. And as a primary care practice, we offer treatment for both acute and chronic conditions while emphasizing prevention, education and optimal health.</p>
  <svg width="24" height="26" viewBox="0 0 24 26" style="margin-top:10px"><path d="M4 3l8 8 8-8M4 13l8 8 8-8" fill="none" stroke="#fff" stroke-width="2.5"/></svg>
</section>

<section class="services">
  <div class="wrap">
    <h2 class="sec-title">Our Best <span class="hl">Services</span></h2>
    <div class="service-grid">
      <div class="service"><div class="service-img" role="img" aria-label="Smiling family" style="background:linear-gradient(135deg,#f3d8b8,#c9a07a)"></div><div class="service-label">Integrative Family Medicine</div></div>
      <div class="service"><div class="service-img" role="img" aria-label="Laboratory sample tubes" style="background:linear-gradient(135deg,#dce8f0,#7aa9c9)"></div><div class="service-label">Functional Medicine</div></div>
      <div class="service"><div class="service-img" role="img" aria-label="Fresh fruits and vegetables" style="background:linear-gradient(135deg,#2e4a1e,#8c9b3a 50%,#3c5a7a)"></div><div class="service-label">Nutrition</div></div>
      <div class="service"><div class="service-img" role="img" aria-label="Measuring tape around a waist" style="background:linear-gradient(135deg,#b9e0ef,#f0c9a8)"></div><div class="service-label">Weight Loss</div></div>
      <div class="service"><div class="service-img" role="img" aria-label="Hands treating a patient's back" style="background:linear-gradient(135deg,#f1d3bf,#c9987a)"></div><div class="service-label">Osteopathic Manipulation</div></div>
      <div class="service"><div class="service-img" role="img" aria-label="Acupuncture needles on a shoulder" style="background:linear-gradient(135deg,#f7e6d8,#d8835a)"></div><div class="service-label">Acupuncture</div></div>
      <div class="service"><div class="service-img" role="img" aria-label="Laboratory test tubes" style="background:linear-gradient(135deg,#d5e9f5,#4a8fbf)"></div><div class="service-label">Labs</div></div>
      <div class="service"><div class="service-img" role="img" aria-label="Person with seasonal allergies" style="background:linear-gradient(135deg,#e9ecc8,#c4a46e)"></div><div class="service-label">Allergy Testing &amp; Treatment</div></div>
    </div>
    <span class="btn view-all">View All</span>
  </div>
</section>

<section class="formula">
  <h2 class="sec-title">Formula for <span class="hl">Good Health</span></h2>
  <div class="habits">
    <div class="habit"><div class="habit-ic"><svg width="56" height="56" viewBox="0 0 56 56"><circle cx="28" cy="28" r="24" fill="none" stroke="#fff" stroke-width="4"/><rect x="12" y="26" width="30" height="6" fill="#fff"/><path d="M11 11l34 34" stroke="#fff" stroke-width="4"/></svg></div><span>No Smoking</span></div>
    <div class="habit"><div class="habit-ic"><svg width="52" height="56" viewBox="0 0 52 56"><path d="M26 16c-6-5-20-4-20 12 0 12 9 24 15 24 3 0 3-2 5-2s2 2 5 2c6 0 15-12 15-24 0-16-14-17-20-12z" fill="#fff"/><path d="M26 16c0-6 3-10 8-12" stroke="#fff" stroke-width="3" fill="none"/></svg></div><span>Healthy Eating</span></div>
    <div class="habit"><div class="habit-ic"><svg width="40" height="60" viewBox="0 0 40 60"><circle cx="20" cy="8" r="6" fill="#fff"/><rect x="12" y="17" width="16" height="22" rx="4" fill="#fff"/><rect x="13" y="38" width="6" height="20" fill="#fff"/><rect x="21" y="38" width="6" height="20" fill="#fff"/></svg></div><span>Healthy Weight</span></div>
    <div class="habit"><div class="habit-ic"><svg width="60" height="52" viewBox="0 0 60 52"><circle cx="30" cy="8" r="6" fill="#fff"/><path d="M30 16v16M12 22l18 8 18-8M8 44c8-8 36-8 44 0" stroke="#fff" stroke-width="5" fill="none" stroke-linecap="round"/></svg></div><span>Daily Exercise</span></div>
    <div class="habit"><div class="habit-ic"><svg width="62" height="44" viewBox="0 0 62 44"><rect x="4" y="4" width="4" height="38" fill="#fff"/><rect x="4" y="26" width="54" height="6" fill="#fff"/><rect x="54" y="26" width="4" height="16" fill="#fff"/><circle cx="16" cy="20" r="5" fill="#fff"/><rect x="24" y="15" width="32" height="10" rx="3" fill="#fff"/></svg></div><span>Adequate Sleep</span></div>
  </div>
</section>

<section class="scheduling">
  <div class="sched-photo" role="img" aria-label="Smiling woman making an OK hand sign"></div>
  <h2 class="sec-title">Online <span class="hl">Scheduling</span></h2>
  <p>Nutrition counselling, Testing like body composition, Basal metabolic rate, CIMT, Breast thermography, VO2 Max testing, Vita Trace<br>Therapies like whole body vibration, Infrared sauna, Exercise with oxygen, Hyperbaric oxygen, Spinal decompression</p>
  <span class="btn">Book a Request</span>
</section>

<section class="about">
  <div class="wrap">
    <h2 class="sec-title">About Us</h2>
    <div class="doctors">
      <div class="doctor">
        <div class="doctor-photo" role="img" aria-label="Portrait of Dr MJ Marlow" style="background:linear-gradient(#c8b8a6,#6e5a48)"></div>
        <div>
          <h3><span>Dr</span> MJ Marlow</h3>
          <p>Margaret "MJ" Marlow has over 20 years of experience as a Registered Nurse in a variety of settings. She was born and mostly raised in Larkston. She completed high school in Oregon and earned her Bachelors of Nursing from the University of Oregon.</p>
          <span class="btn">Know More</span>
        </div>
      </div>
      <div class="doctor">
        <div class="doctor-photo" role="img" aria-label="Portrait of Dr Pryce" style="background:linear-gradient(#e4e7ea,#7d8fa3)"></div>
        <div>
          <h3><span>Dr</span> Pryce</h3>
          <p>Margaret "MJ" Marlow has over 20 years of experience as a Registered Nurse in a variety of settings. She was born and mostly raised in Larkston. She completed high school in Oregon and earned her Bachelors of Nursing from the University of Oregon.</p>
          <span class="btn">Know More</span>
        </div>
      </div>
    </div>
  </div>
</section>

<section class="testimonial">
  <h2 class="sec-title">What Our <span class="hl">Client Say</span></h2>
  <div class="client-photo" role="img" aria-label="Client portrait"></div>
  <blockquote>" Lorem Ipsum is simply dummy text of the printing and typesetting industry. Lorem Ipsum has been the industry's standard dummy text ever since the 1500s, when an unknown printer took a galley of type and scrambled it to make a type specimen book. It has survived not only five centuries, but also the leap into electronic typesetting, remaining essentially unchanged. "</blockquote>
  <div class="client-name">Client Name</div>
  <div class="dots"><i class="on"></i><i></i><i></i><i></i></div>
</section>

<section class="widgets">
  <div class="wrap">
    <div class="widget-row">
      <div class="widget">
        <h4>Feature</h4>
        <div class="feature-list">
          <div class="feature-item"><i></i>Are you toxic questionnaire?</div>
          <div class="feature-item"><i></i>Take our hormone quiz to find out if hormones are affecting your health.</div>
        </div>
        <div class="quiz-btn"><b>Questionnaire</b><em><svg width="12" height="20" viewBox="0 0 12 20"><path d="M2 2l8 8-8 8" stroke="#fff" stroke-width="3" fill="none"/></svg></em></div>
      </div>
      <div class="widget">
        <h4>Blog</h4>
        <div class="blog-list">
          <div class="post"><div class="post-img" role="img" aria-label="Blog post photo" style="background:linear-gradient(135deg,#5b3a22,#c99b6a)"></div><div><h5>LOREM IPSUM TEXT.</h5><p>Lorem Ipsum is simply dummy text of the printing and typesetting industry.</p></div></div>
          <div class="post"><div class="post-img" role="img" aria-label="Blog post photo" style="background:linear-gradient(135deg,#f3dccb,#c77d5a)"></div><div><h5>LOREM IPSUM TEXT.</h5><p>Lorem Ipsum is simply dummy text of the printing and typesetting industry.</p></div></div>
          <div class="post"><div class="post-img" role="img" aria-label="Blog post photo" style="background:linear-gradient(135deg,#cfe3f1,#e3c4a6)"></div><div><h5>LOREM IPSUM TEXT.</h5><p>Lorem Ipsum is simply dummy text of the printing and typesetting industry.</p></div></div>
        </div>
      </div>
      <div class="widget">
        <h4>Linkpage Feed</h4>
        <div class="feed">
          <div class="feed-note">Be the first of your friends to like this</div>
          <div class="feed-box">
            <div class="feed-head"><div class="feed-thumb" role="img" aria-label="Page thumbnail"></div><div><b>Bright Oak Family Medicine</b><span>December 18 at 6:11pm</span></div></div>
            <div class="feed-text">Food for Thought</div>
            <div class="feed-img" role="img" aria-label="Bowl of fresh berries"></div>
            <div class="feed-foot"><span>Embed</span><span>View on Linkpage</span></div>
          </div>
        </div>
      </div>
    </div>
  </div>
</section>

<footer class="site-footer">
  <div class="wrap">
    <div class="foot-cols">
      <div class="foot-col">
        <h6>Usefull Links</h6>
        <ul class="links"><li>Home</li><li>About Us</li><li>Services</li><li>Resources</li><li>Faq</li><li>Current Patients</li><li>New Patients</li><li>OakWell Membership</li><li>Contact Us</li></ul>
      </div>
      <div class="foot-col">
        <h6>Get in Touch</h6>
        <div class="contact-row"><svg width="20" height="18" viewBox="0 0 20 18"><path d="M2 8l8-6 8 6v9H2z" fill="none" stroke="#fff" stroke-width="2"/></svg><span>BRIGHT OAK<br>482 Meadow Row, Cedar Falls, TX<br>70000</span></div>
        <div class="contact-row"><svg width="20" height="18" viewBox="0 0 24 24"><path d="M6.6 10.8a15 15 0 006.6 6.6l2.2-2.2a1 1 0 011-.25 11.4 11.4 0 003.6.57 1 1 0 011 1V20a1 1 0 01-1 1A17 17 0 013 4a1 1 0 011-1h3.5a1 1 0 011 1 11.4 11.4 0 00.57 3.6 1 1 0 01-.25 1z" fill="#fff"/></svg><span>(555) 214-7730</span></div>
        <div class="contact-row"><svg width="20" height="18" viewBox="0 0 20 18"><rect x="4" y="1" width="12" height="5" fill="none" stroke="#fff" stroke-width="2"/><rect x="1" y="6" width="18" height="8" fill="none" stroke="#fff" stroke-width="2"/><rect x="4" y="11" width="12" height="6" fill="#fff"/></svg><span>(555) 214-7731</span></div>
        <div class="contact-row"><svg width="20" height="18" viewBox="0 0 20 18"><rect x="1" y="3" width="18" height="12" fill="none" stroke="#fff" stroke-width="2"/><path d="M1 3l9 7 9-7" fill="none" stroke="#fff" stroke-width="2"/></svg><span>info@brightoakfm.com</span></div>
      </div>
      <div class="foot-col">
        <h6>Opening Hours</h6>
        <div class="hours-row"><i></i><span>Monday</span><span>8am - 6pm</span></div>
        <div class="hours-row"><i></i><span>Tuesday</span><span>8am - 6pm</span></div>
        <div class="hours-row"><i></i><span>Wednesday</span><span>8am - 6pm</span></div>
        <div class="hours-row"><i></i><span>Thursday</span><span>8am - 6pm</span></div>
        <div class="hours-row"><i></i><span>Friday</span><span>8am - 6pm</span></div>
        <p class="hours-note">The Office is closed from 12 - 1 for lunch Most insurances accepted</p>
      </div>
      <div class="foot-col news">
        <h6>Newsletter</h6>
        <p>Would you like to receive exclusive access to articles, white papers and our regular monthly newsletter?</p>
        <div class="field">Enter Email Id</div>
        <span class="btn">Subscribe</span>
      </div>
    </div>
  </div>
</footer>
<div class="bottom-bar">© 2016 <b>BRIGHT OAK FAMILY MEDICINE</b> • All rights reserved</div>

</body>
</html>
```